Small boutique multi-family apartment developer needs premium website design.

We are a growing real estate development company specializing in multi family apartment development. Our company Mireval Stone Development focuses on passive real estate investors looking to maximize their current real estate portfolio by allowing us to develop and reposition their current properties allowing them more cashflow while we are also able to take over the management of their asset in order to ensure optimal performance on a consistent basis.

```html
<!DOCTYPE html>
<html lang="en">
<head>
<meta charset="utf-8">
<title>Mireval Stone Development</title>
<link href="https://fonts.googleapis.com/css2?family=Poppins:wght@300;400;500;600;700&display=swap" rel="stylesheet">
<style>
:root{
  --ink:#1d1d1d;
  --dark:#1f1f1f;
  --white:#ffffff;
  --accent:#7fa7d4;
  --accent-deep:#6f95c4;
  --muted:#6b6b6b;
  --star:#f2a23a;
  --line:#d9d9d9;
}
*{margin:0;padding:0;box-sizing:border-box}
html,body{width:1200px;height:4762px;overflow:hidden}
body{font-family:"Poppins",sans-serif;color:var(--ink);background:var(--white);position:relative}
.abs{position:absolute}
.photo{position:absolute}

/* header / hero */
.hero{position:absolute;left:0;top:0;width:1200px;height:841px;
  background:linear-gradient(180deg,#587db0 0%,#8ea8c8 40%,#c6d2de 62%,#b79a82 80%,#8c6a52 100%)}
.logo{font-weight:600;color:var(--white);font-size:20px}
.hero .logo{left:131px;top:22px}
.nav{left:534px;top:27px;display:flex;gap:20px;font-size:12px;color:var(--white);font-weight:500}
.nav .active{border-bottom:2px solid var(--white);padding-bottom:3px}
.btn-dark{background:var(--dark);color:var(--white);font-weight:600;font-size:12px;display:flex;align-items:center;justify-content:center}
.contact-btn{left:941px;top:17px;width:124px;height:37px}
.hero-title{left:0;width:1200px;top:146px;text-align:center;color:var(--white);font-weight:700;font-size:45px;line-height:49px}
.hero-sub{left:330px;width:540px;top:262px;text-align:center;color:var(--white);font-size:12px;line-height:20px}
.hero-btn{left:512px;top:316px;width:176px;height:37px}

/* stats */
.stats{left:0;top:841px;width:1200px;height:178px;background:var(--dark)}
.stat{position:absolute;top:46px;width:200px;text-align:center;color:var(--white)}
.stat b{display:block;font-weight:600;font-size:44px;line-height:54px}
.stat b span{color:var(--accent)}
.stat small{font-size:13px}

/* about */
.about-title{left:176px;top:1165px;font-size:35px;line-height:40px;font-weight:400}
.about-title strong{font-weight:700}
.about-text{left:176px;top:1262px;width:410px;font-size:11.5px;line-height:19.5px;color:var(--muted)}
.about-btn{left:176px;top:1444px;width:251px;height:37px;background:var(--accent-deep);color:var(--white);font-size:11.5px;font-weight:600;display:flex;align-items:center;justify-content:center}
.about-frame{left:686px;top:1148px;width:296px;height:390px;border:7px solid var(--accent-deep)}

/* sections */
.section-title{font-size:35px;font-weight:400;line-height:44px}
.section-title strong{font-weight:700}
.services-title{left:129px;top:1660px}
.arrow-btn{width:46px;height:46px;border-radius:50%;display:flex;align-items:center;justify-content:center}
.dark-band{left:0;top:1980px;width:1200px;height:1025px;background:var(--dark)}
.card{position:absolute;top:1771px;width:381px;height:509px;background:var(--white);box-shadow:0 6px 18px rgba(0,0,0,.12)}
.card .img{position:absolute;left:0;top:0;width:381px;height:291px}
.card h3{position:absolute;left:18px;top:318px;font-size:19px;font-weight:600;white-space:nowrap}
.card p{position:absolute;left:18px;top:356px;width:345px;font-size:11.5px;line-height:20px;color:var(--muted)}

.process-title{left:0;width:1200px;top:2360px;text-align:center;color:var(--white)}
.process-line{left:226px;top:2477px;width:763px;height:1px;background:#8a8a8a}
.step{position:absolute;top:2448px;width:160px;text-align:center}
.step .icon{width:59px;height:59px;margin:0 auto;background:var(--white);display:flex;align-items:center;justify-content:center}
.step .icon.on{background:var(--accent-deep)}
.step span{display:block;margin-top:16px;color:var(--white);font-size:14px;font-weight:500}

.portfolio-title{left:0;width:1200px;top:3085px;text-align:center}

.clients-title{left:0;width:1200px;top:3888px;text-align:center}
.clients-sub{left:280px;width:640px;top:3946px;text-align:center;font-size:13px;line-height:20px;color:var(--muted)}
.t-card{position:absolute;top:4005px;width:322px;height:266px;background:var(--white);box-shadow:0 8px 26px rgba(0,0,0,.1)}
.t-card .avatar{position:absolute;left:22px;top:22px;width:64px;height:64px;border-radius:50%;background:linear-gradient(135deg,#8a8a8a,#3e3e3e)}
.t-card .name{position:absolute;left:100px;top:34px;font-size:15px;font-weight:600}
.t-card .role{position:absolute;left:100px;top:58px;font-size:12.5px;color:var(--muted)}
.t-card .quote{position:absolute;right:22px;top:14px;font-size:54px;line-height:54px;font-weight:700;color:var(--accent)}
.t-card .stars{position:absolute;left:22px;top:110px;display:flex;gap:8px}
.t-card p{position:absolute;left:22px;top:162px;width:280px;font-size:11.5px;line-height:20px;color:var(--muted)}
.dots{left:536px;top:4295px;display:flex;gap:8px}
.dots i{display:block;width:36px;height:4px;background:var(--accent-deep)}

/* footer */
.footer{left:0;top:4391px;width:1200px;height:371px;background:var(--dark);color:var(--white)}
.footer .logo{position:absolute;left:129px;top:135px;font-size:38px;font-weight:600}
.f-head{position:absolute;top:56px;font-size:22px;font-weight:500}
.f-links{position:absolute;left:427px;top:105px;font-size:13.5px;line-height:24px}
.f-contact{position:absolute;left:623px;top:106px;font-size:13.5px;line-height:19px}
.f-contact .item{margin-bottom:8px}
.f-contact b{font-weight:600;display:flex;align-items:center;gap:6px}
.f-contact .val{padding-left:18px}
.socials{position:absolute;left:869px;top:104px;display:flex;gap:10px}
.socials i{display:block;width:41px;height:41px;border-radius:50%;background:#3c3c3c}
.f-rule{position:absolute;left:88px;top:306px;width:1024px;height:1px;background:#444}
.copy{position:absolute;left:0;width:1200px;top:328px;text-align:center;font-size:13px}
.to-top{position:absolute;left:1132px;top:278px;width:40px;height:40px;border-radius:50%;background:var(--accent-deep);display:flex;align-items:center;justify-content:center}
</style>
</head>
<body>

<!-- hero -->
<div class="hero" role="img" aria-label="Modern white two-storey house with wooden cladding and deck, set against a soft blue sky"></div>
<div class="abs logo hero-logo" style="left:131px;top:20px">Logo Here</div>
<nav class="abs nav">
  <span class="active">Home</span><span>About Us</span><span>Services</span><span>Our Process</span><span>Portfolio</span>
</nav>
<div class="abs btn-dark contact-btn">Contact Us</div>
<h1 class="abs hero-title">Expanding Your Portfolio with Expert<br>Development</h1>
<p class="abs hero-sub">Specializing in multi-family apartment development, we help investors enhance their properties for greater returns.</p>
<div class="abs btn-dark hero-btn">Explore Our Services</div>

<!-- stats -->
<section class="abs stats">
  <div class="stat" style="left:144px"><b>128<span>K</span></b><small>Renters</small></div>
  <div class="stat" style="left:381px"><b>300<span>+</span></b><small>Specialists</small></div>
  <div class="stat" style="left:621px"><b>78<span>%</span></b><small>Yearly Growth</small></div>
  <div class="stat" style="left:854px"><b>10<span>K+</span></b><small>Properties</small></div>
</section>

<!-- about -->
<h2 class="abs about-title">Your Partner in <strong>Real<br>Estate</strong> Growth</h2>
<p class="abs about-text">At Mireval Stone Development, we partner with passive real estate investors to maximize the potential of their properties. Our team specializes in multi-family apartment development, repositioning, and management to deliver consistent performance and increased cash flow for our clients. we transform your real estate investments into high-performing assets. Our expert team specializes in multi-family development and management, maximizing portfolio value and cash flow.</p>
<div class="abs about-btn">Learn More About Our Approach</div>
<div class="abs about-frame"></div>
<div class="photo" style="left:645px;top:1107px;width:254px;height:293px;background:linear-gradient(160deg,#9c7562,#c9c3bc 50%,#6e7f92)" role="img" aria-label="Senior architect holding rolled plans in front of apartment towers"></div>
<div class="photo" style="left:769px;top:1283px;width:255px;height:290px;background:linear-gradient(160deg,#d8dee4,#8d96a0 55%,#5a6470)" role="img" aria-label="Two designers reviewing an architectural model"></div>

<!-- services -->
<div class="abs dark-band"></div>
<h2 class="abs section-title services-title">Our <strong>Services</strong></h2>
<div class="abs arrow-btn" style="left:966px;top:1660px;background:#8a8a8a">
  <svg width="16" height="16" viewBox="0 0 16 16"><path d="M13 8H3M7 4L3 8l4 4" fill="none" stroke="#fff" stroke-width="1.6"/></svg>
</div>
<div class="abs arrow-btn" style="left:1018px;top:1660px;background:var(--accent)">
  <svg width="16" height="16" viewBox="0 0 16 16"><path d="M3 8h10M9 4l4 4-4 4" fill="none" stroke="#fff" stroke-width="1.6"/></svg>
</div>

<div class="card" style="left:131px">
  <div class="img" style="background:linear-gradient(160deg,#d5d3cf,#8f8a84 60%,#4d4a47)" role="img" aria-label="Three men working over building plans at a table"></div>
  <h3>Development and Repositioning</h3>
  <p>Our expertise in multi-family apartment development allows us to transform your existing properties into modern, high-performing assets. Whether through new construction or repositioning, we help you increase property value and cash flow.</p>
</div>
<div class="card" style="left:540px">
  <div class="img" style="background:linear-gradient(160deg,#c9bfb2,#b89a5c 55%,#6f6458)" role="img" aria-label="Team of four discussing documents around a table"></div>
  <h3>Asset Management</h3>
  <p>With our hands-on management approach, we ensure your properties are consistently optimized for performance. From tenant management to maintenance, we take care of every detail, so you can enjoy passive income with peace of mind.</p>
</div>
<div class="card" style="left:949px">
  <div class="img" style="background:linear-gradient(160deg,#55683f,#8a8f84 55%,#c9c9c6)" role="img" aria-label="Colleagues reviewing charts at an office desk"></div>
  <h3>Development and Repositioning</h3>
  <p>Our expertise in multi-family apartment development allows us to transform your existing properties into modern, high-performing assets. Whether through new construction or repositioning, we help you increase property value and cash flow.</p>
</div>

<!-- process -->
<h2 class="abs section-title process-title">Our <strong>Process</strong></h2>
<div class="abs process-line"></div>
<div class="step" style="left:146px"><div class="icon on">
  <svg width="34" height="34" viewBox="0 0 34 34" fill="none" stroke="#fff" stroke-width="1.6"><circle cx="17" cy="11" r="4"/><circle cx="8" cy="15" r="3"/><circle cx="26" cy="15" r="3"/><path d="M10 27c0-5 3-8 7-8s7 3 7 8M3 27c0-4 2-6 5-6M31 27c0-4-2-6-5-6"/></svg>
</div><span>Consultation</span></div>
<div class="step" style="left:330px"><div class="icon">
  <svg width="34" height="34" viewBox="0 0 34 34" fill="none" stroke="#333" stroke-width="1.6"><rect x="5" y="4" width="20" height="26"/><path d="M9 10h12M9 15h8M9 24l4-4 3 3 5-5"/><circle cx="24" cy="22" r="5"/><path d="M28 26l3 3"/></svg>
</div><span>Strategy</span></div>
<div class="step" style="left:517px"><div class="icon">
  <svg width="34" height="34" viewBox="0 0 34 34" fill="none" stroke="#333" stroke-width="1.6"><rect x="4" y="6" width="26" height="20"/><path d="M4 11h26M12 16l-3 3 3 3M18 16l3 3-3 3"/><circle cx="25" cy="24" r="4"/></svg>
</div><span>Development</span></div>
<div class="step" style="left:721px"><div class="icon">
  <svg width="34" height="34" viewBox="0 0 34 34" fill="none" stroke="#333" stroke-width="1.6"><circle cx="14" cy="14" r="5"/><path d="M14 5v3M14 20v3M5 14h3M20 14h3M8 8l2 2M18 18l2 2M20 8l-2 2M8 20l2-2"/><circle cx="24" cy="24" r="4"/><path d="M24 17v2M24 29v2M17 24h2M29 24h2"/></svg>
</div><span>Management</span></div>
<div class="step" style="left:909px"><div class="icon">
  <svg width="34" height="34" viewBox="0 0 34 34" fill="none" stroke="#333" stroke-width="1.6"><rect x="4" y="5" width="26" height="19"/><path d="M13 29h8M17 24v5M9 19l5-5 4 3 7-7"/><rect x="8" y="9" width="6" height="4"/></svg>
</div><span>Visual</span></div>
<div class="photo" style="left:131px;top:2598px;width:936px;height:342px;background:linear-gradient(180deg,#7fa3cf 0%,#c5d4e4 50%,#e8e8e6 72%,#9fa6ad 100%)" role="img" aria-label="Minimal white modern villa with a white tree on snowy terraced steps"></div>

<!-- portfolio -->
<h2 class="abs section-title portfolio-title">Our <strong>Portfolio</strong></h2>
<div class="photo" style="left:128px;top:3164px;width:299px;height:212px;background:linear-gradient(160deg,#e2e2e0,#8c7a6a 60%,#4b4640)" role="img" aria-label="Two designers examining an architectural model"></div>
<div class="photo" style="left:128px;top:3397px;width:299px;height:408px;background:linear-gradient(170deg,#8a6f56,#c8c3bb 45%,#6e7e96)" role="img" aria-label="Engineer in a hard hat sketching plans beside building models"></div>
<div class="photo" style="left:447px;top:3164px;width:300px;height:314px;background:linear-gradient(170deg,#e9ecef,#c2c6cb 55%,#9aa0a8)" role="img" aria-label="White apartment building with balconies"></div>
<div class="photo" style="left:447px;top:3493px;width:300px;height:312px;background:linear-gradient(170deg,#8fb3dc,#d0d4d8 50%,#4a4e55)" role="img" aria-label="Woman in a hard hat in front of an apartment tower under construction"></div>
<div class="photo" style="left:765px;top:3164px;width:300px;height:212px;background:linear-gradient(160deg,#7e9cc4,#b7c4d2 50%,#3c5f86)" role="img" aria-label="Scale model of a city block with towers"></div>
<div class="photo" style="left:765px;top:3397px;width:300px;height:408px;background:linear-gradient(170deg,#e6e6e4,#bfc2c6 50%,#5e6d82)" role="img" aria-label="Architect standing beside a white tower model"></div>

<!-- testimonials -->
<h2 class="abs section-title clients-title">What our <strong>Clients</strong> says</h2>
<p class="abs clients-sub">It is a long established fact that a reader will be distracted by the readable content of a page when looking at its layout.</p>

<div class="t-card" style="left:94px">
  <div class="avatar" role="img" aria-label="Client portrait"></div>
  <div class="name">Owen Parrish</div><div class="role">Client</div>
  <div class="quote">”</div>
  <div class="stars">
    <svg width="24" height="24" viewBox="0 0 24 24"><path d="M12 2l3 7 7 .6-5.4 4.7 1.7 7.2L12 17.7 5.7 21.5l1.7-7.2L2 9.6 9 9z" fill="#f2a23a"/></svg>
    <svg width="24" height="24" viewBox="0 0 24 24"><path d="M12 2l3 7 7 .6-5.4 4.7 1.7 7.2L12 17.7 5.7 21.5l1.7-7.2L2 9.6 9 9z" fill="#f2a23a"/></svg>
    <svg width="24" height="24" viewBox="0 0 24 24"><path d="M12 2l3 7 7 .6-5.4 4.7 1.7 7.2L12 17.7 5.7 21.5l1.7-7.2L2 9.6 9 9z" fill="#f2a23a"/></svg>
    <svg width="24" height="24" viewBox="0 0 24 24"><path d="M12 2l3 7 7 .6-5.4 4.7 1.7 7.2L12 17.7 5.7 21.5l1.7-7.2L2 9.6 9 9z" fill="#f2a23a"/></svg>
    <svg width="24" height="24" viewBox="0 0 24 24"><path d="M12 2l3 7 7 .6-5.4 4.7 1.7 7.2L12 17.7 5.7 21.5l1.7-7.2L2 9.6 9 9z" fill="#f2a23a"/></svg>
  </div>
  <p>It is a long established fact that a reader will be distracted by the readable content of a page when looking at its layout.</p>
</div>
<div class="t-card" style="left:438px">
  <div class="avatar" role="img" aria-label="Client portrait"></div>
  <div class="name">Lena Marsh</div><div class="role">Client</div>
  <div class="quote">”</div>
  <div class="stars">
    <svg width="24" height="24" viewBox="0 0 24 24"><path d="M12 2l3 7 7 .6-5.4 4.7 1.7 7.2L12 17.7 5.7 21.5l1.7-7.2L2 9.6 9 9z" fill="#f2a23a"/></svg>
    <svg width="24" height="24" viewBox="0 0 24 24"><path d="M12 2l3 7 7 .6-5.4 4.7 1.7 7.2L12 17.7 5.7 21.5l1.7-7.2L2 9.6 9 9z" fill="#f2a23a"/></svg>
    <svg width="24" height="24" viewBox="0 0 24 24"><path d="M12 2l3 7 7 .6-5.4 4.7 1.7 7.2L12 17.7 5.7 21.5l1.7-7.2L2 9.6 9 9z" fill="#f2a23a"/></svg>
    <svg width="24" height="24" viewBox="0 0 24 24"><path d="M12 2l3 7 7 .6-5.4 4.7 1.7 7.2L12 17.7 5.7 21.5l1.7-7.2L2 9.6 9 9z" fill="#f2a23a"/></svg>
    <svg width="24" height="24" viewBox="0 0 24 24"><path d="M12 2l3 7 7 .6-5.4 4.7 1.7 7.2L12 17.7 5.7 21.5l1.7-7.2L2 9.6 9 9z" fill="#f2a23a"/></svg>
  </div>
  <p>It is a long established fact that a reader will be distracted by the readable content of a page when looking at its layout.</p>
</div>
<div class="t-card" style="left:782px">
  <div class="avatar" role="img" aria-label="Client portrait"></div>
  <div class="name">Owen Parrish</div><div class="role">Client</div>
  <div class="quote">”</div>
  <div class="stars">
    <svg width="24" height="24" viewBox="0 0 24 24"><path d="M12 2l3 7 7 .6-5.4 4.7 1.7 7.2L12 17.7 5.7 21.5l1.7-7.2L2 9.6 9 9z" fill="#f2a23a"/></svg>
    <svg width="24" height="24" viewBox="0 0 24 24"><path d="M12 2l3 7 7 .6-5.4 4.7 1.7 7.2L12 17.7 5.7 21.5l1.7-7.2L2 9.6 9 9z" fill="#f2a23a"/></svg>
    <svg width="24" height="24" viewBox="0 0 24 24"><path d="M12 2l3 7 7 .6-5.4 4.7 1.7 7.2L12 17.7 5.7 21.5l1.7-7.2L2 9.6 9 9z" fill="#f2a23a"/></svg>
    <svg width="24" height="24" viewBox="0 0 24 24"><path d="M12 2l3 7 7 .6-5.4 4.7 1.7 7.2L12 17.7 5.7 21.5l1.7-7.2L2 9.6 9 9z" fill="#f2a23a"/></svg>
    <svg width="24" height="24" viewBox="0 0 24 24"><path d="M12 2l3 7 7 .6-5.4 4.7 1.7 7.2L12 17.7 5.7 21.5l1.7-7.2L2 9.6 9 9z" fill="#f2a23a"/></svg>
  </div>
  <p>It is a long established fact that a reader will be distracted by the readable content of a page when looking at its layout.</p>
</div>
<div class="abs dots"><i></i><i></i><i></i><i></i></div>

<!-- footer -->
<footer class="abs footer">
  <div class="logo">Logo Here</div>
  <div class="f-head" style="left:427px">Quick link</div>
  <div class="f-links">Home<br>About Us<br>Services<br>Our Process<br>Portfolio<br>Contact Us</div>
  <div class="f-head" style="left:623px">Contact us</div>
  <div class="f-contact">
    <div class="item"><b><svg width="12" height="12" viewBox="0 0 24 24"><path d="M6 2l4 4-2 3c1 3 4 6 7 7l3-2 4 4-3 4C10 22 2 14 2 5z" fill="#fff"/></svg>Phone</b><div class="val">+(123) 456-789</div></div>
    <div class="item"><b><svg width="12" height="12" viewBox="0 0 24 24"><rect x="2" y="5" width="20" height="14" fill="#fff"/><path d="M2 5l10 8 10-8" fill="none" stroke="#1f1f1f" stroke-width="2"/></svg>Email</b><div class="val">info@Example.com</div></div>
    <div class="item"><b><svg width="12" height="12" viewBox="0 0 24 24"><path d="M12 2a7 7 0 0 0-7 7c0 5 7 13 7 13s7-8 7-13a7 7 0 0 0-7-7z" fill="#fff"/><circle cx="12" cy="9" r="2.5" fill="#1f1f1f"/></svg>Location</b><div class="val">some gose address<br>link here 0000</div></div>
  </div>
  <div class="f-head" style="left:869px">Follow us</div>
  <div class="socials" aria-label="Social media links"><i></i><i></i><i></i><i></i></div>
  <div class="f-rule"></div>
  <div class="copy">© 2024 Mireval Stone. All rights reserved.</div>
  <div class="to-top"><svg width="14" height="14" viewBox="0 0 14 14"><path d="M3 9l4-4 4 4" fill="none" stroke="#fff" stroke-width="1.8"/></svg></div>
</footer>

</body>
</html>
```